Automotive debt collection business need several banners for new website

We are a debt recovery company called Quellton Recoveries Ltd who work specifically within the car automotive industry acting on behalf of our clients to recover debt which is owed to them. The advantage to using a company such as QRL is that it allows our clients the ability to outsource the work, removing the headache of dealing with the general public and reduces internal staff/overhead costs.
We collect various types of debt including:
Excess Mileage - this is charged when an individual has exceeded their permitted mileage allowance. This is calculated on a pence per mile basis on the mileage over the limit set when the contract was signed.
Damage - charged when a vehicle sustains more damage than is permitted within the contract. Damage could be dents to bodywork, large scratches, torn seats etc. Every area of damage over and above the allowed levels is detailed via a 'Damage Report' and a cost associated to that area of damage. The individual costs are then added up and a total charge formulated. The customer is liable to pay these charges as they have not cared for the vehicle in the appropriate manner whilst under their control
End of Contract Arrears - Once a contract ends and a vehicle is returned to our clients, there may be other charges that need to be repaid that remain outstanding.
We collect debt using a simple process. 1 - The customer is sent a letter as soon as the vehicle is collected advising them of the value of the debt. 2 - A few days later, we attempt to make contact via telephone or email. 3 - Once we contact the customer, we explain the debt and how the figure has been formulated (which is also explain in their letters). 4 - We negotiate (where appropriate) and agree a settlement figure. 5 - The customer pays the debt either in one installment over over a short payment plan.
Our new website (test URL only - http://testing.quelltonrecoveries.co.uk/) has a dual purpose. Firstly its to help promote our services to new clients who may be in the market for an alternative supplier (as far as we are aware, we are the only dedicated automotive debt collection company in the UK) and secondly, as a site to help those who owe money to pay and understand who we are (and that we are a registered, legal debt collection company)
Unlike other debt collection websites, we do not want generic images of people shaking hands, smiling etc. We want the images to be visually striking and make the website stand out from the competition. We are happy for these to be graphics rather than images.
We require some visual banners to represent what we do as a business and to emphasis that we specifically collect debt for the automotive sector.
These are websites that contain banners that we are NOT looking for:
http://uk.vabrix-partners.com/consumers/contact-data-working-hours/ - bland images of call centers/random people on phones etc
http://www.almsfield.com/client/
These are websites that contain banners that we class as OK:
http://www.norvanta.co.uk/business-services/debt-collection.html - fairly clear way of explaining their services
http://www.estatedues.co.uk/ - a slightly different slant using non-related images to explain what they can and cant do
http://www.pkwholdings.com/home/#.UhNNeD98CL0 - uses text to text banners to explain their offering
We require:
x4 - 870px X 500px - these will appear on the main homepage and rotate
x2 - 270px X 240px - static images that will to the right of the home page. One image needs to indicate some type of payment method as its a link to our online payment system, the second image refers to our other services (see the appropriate page on the website) these additional services include asset recovery, inspection, bespoke software solutions for the asset industry and auction disposal
x3 - 90px X 90px - Static images to represent payment methods that include cheque/card/bank transfer (see website for more info)
Our corporate colours are Black/Red/Grey
Depending on the designs received, we expect 2 rounds of modifications and we will advise those designers that have not been successful with positive feedback. We guarantee to pay the successful designer but work must be completed and ALL requested material produced and approved.

```html
<!DOCTYPE html>
<html lang="en">
<head>
<meta charset="utf-8">
<title>Quellton Recoveries Ltd – Payment Tiles</title>
<link rel="stylesheet" href="https://fonts.googleapis.com/css2?family=Arimo:wght@400;700&display=swap">
<style>
  :root {
    --brand-red: #a82025;
    --panel-grey: #e6e6e6;
    --ink: #111111;
    --white: #ffffff;
    --illus-warm: #b3372b;
    --illus-cool: #2a8fc8;
    --illus-yellow: #f7c23a;
    --illus-dark: #2b2624;
  }
  * { margin: 0; padding: 0; box-sizing: border-box; }
  html, body {
    width: 1200px;
    height: 851px;
    overflow: hidden;
    background: var(--white);
  }
  body {
    position: relative;
    font-family: "Arimo", Arial, sans-serif;
    color: var(--ink);
  }
  .tile {
    position: absolute;
    width: 320px;
    height: 320px;
  }
  .tile--feature { background: var(--panel-grey); }
  .tile--method { background: var(--brand-red); }

  .tile-label {
    position: absolute;
    left: 0;
    right: 0;
    color: var(--white);
    font-weight: 700;
    text-align: center;
    text-transform: uppercase;
    letter-spacing: 0.2px;
  }
  .feature-band {
    position: absolute;
    left: 0;
    width: 320px;
    background: var(--brand-red);
    display: flex;
    align-items: center;
    justify-content: center;
  }
  .feature-band .tile-label {
    position: static;
    font-size: 30px;
    line-height: 0.98;
  }
  .illustration {
    position: absolute;
  }
  .illustration--card-hand {
    left: 62px; top: 112px; width: 256px; height: 208px;
    background: linear-gradient(135deg, var(--illus-warm) 0%, var(--illus-warm) 45%, var(--illus-cool) 100%);
    opacity: 0.85;
  }
  .illustration--megaphone {
    left: 24px; top: 100px; width: 262px; height: 220px;
    background: linear-gradient(160deg, var(--illus-yellow) 0%, var(--illus-yellow) 55%, var(--illus-warm) 85%, var(--illus-dark) 100%);
    opacity: 0.85;
  }
  .method-label {
    top: 28px;
    font-size: 29px;
  }
  .method-icon {
    position: absolute;
    left: 0;
    top: 0;
    width: 320px;
    height: 320px;
  }
  .size-note {
    position: absolute;
    font-size: 24px;
    color: var(--ink);
  }
</style>
</head>
<body>

  <!-- Feature tiles -->
  <section class="tile tile--feature" style="left:218px; top:35px;">
    <div class="feature-band" style="top:28px; height:60px;">
      <span class="tile-label">Payment Portal</span>
    </div>
    <div class="illustration illustration--card-hand" role="img" aria-label="Illustration of a hand in a suit sleeve holding up a blue payment card"></div>
  </section>
  <p class="size-note" style="left:218px; top:372px;">270px X 240px</p>

  <section class="tile tile--feature" style="left:662px; top:35px;">
    <div class="feature-band" style="top:28px; height:72px;">
      <span class="tile-label">Additional<br>Services</span>
    </div>
    <div class="illustration illustration--megaphone" role="img" aria-label="Illustration of a hand in a suit sleeve raising a yellow megaphone with sound bursts"></div>
  </section>
  <p class="size-note" style="left:662px; top:372px;">270px X 240px</p>

  <!-- Payment method tiles -->
  <section class="tile tile--method" style="left:26px; top:460px;">
    <span class="tile-label method-label">Card Payment</span>
    <svg class="method-icon" viewBox="0 0 267 267" aria-hidden="true">
      <g transform="rotate(14 158 128)">
        <rect x="85" y="72" width="150" height="108" rx="8" fill="#fff"/>
        <rect x="85" y="90" width="150" height="16" fill="#a82025"/>
      </g>
      <rect x="34" y="131" width="163" height="118" rx="14" fill="#a82025"/>
      <rect x="38" y="135" width="155" height="110" rx="12" fill="#fff"/>
      <rect x="143" y="162" width="28" height="28" rx="5" fill="#a82025"/>
      <rect x="56" y="214" width="74" height="10" fill="#a82025"/>
    </svg>
  </section>
  <p class="size-note" style="left:26px; top:792px;">270px X 240px</p>

  <section class="tile tile--method" style="left:446px; top:460px;">
    <span class="tile-label method-label">Cheque Payment</span>
    <svg class="method-icon" viewBox="0 0 267 267" aria-hidden="true">
      <rect x="16" y="97" width="227" height="110" fill="none" stroke="#fff" stroke-width="5"/>
      <rect x="14" y="95" width="231" height="12" fill="#fff"/>
      <rect x="31" y="128" width="52" height="5" fill="#fff"/>
      <rect x="31" y="141" width="148" height="5" fill="#fff"/>
      <rect x="186" y="128" width="42" height="18" fill="#fff"/>
      <rect x="58" y="174" width="70" height="5" fill="#fff"/>
      <rect x="58" y="186" width="70" height="5" fill="#fff"/>
    </svg>
  </section>
  <p class="size-note" style="left:446px; top:792px;">270px X 240px</p>

  <section class="tile tile--method" style="left:838px; top:460px;">
    <span class="tile-label method-label">Bank Payment</span>
    <svg class="method-icon" viewBox="0 0 267 267" aria-hidden="true">
      <polygon points="130,78 208,124 52,124" fill="#fff"/>
      <circle cx="130" cy="106" r="8" fill="#a82025"/>
      <rect x="57" y="128" width="146" height="9" fill="#fff"/>
      <rect x="72" y="141" width="22" height="46" fill="#fff"/>
      <rect x="119" y="141" width="22" height="46" fill="#fff"/>
      <rect x="166" y="141" width="22" height="46" fill="#fff"/>
      <rect x="66" y="191" width="128" height="12" rx="2" fill="#fff"/>
      <rect x="52" y="208" width="156" height="13" rx="3" fill="#fff"/>
    </svg>
  </section>
  <p class="size-note" style="left:838px; top:792px;">270px X 240px</p>

</body>
</html>
```